Flyer for "Master the Mash Tun Basics" course

NEEDED: A6 flyer designed to advertise my first training course:
Intro to craft beer brewing

The company brand identity was recently bought from Pixel Harbor and it can be seen, with colour scheme on our website: www.TinmoorKettle.com.

The flyer is to be in line with my current brand identity and have a strong hook to push people to our site.

The flyer's goal is to get people to visit the site to book on a craft beer brewing training course. The info available to be included, although you have the freedom to include as much or as little as you see fit:

Currently a sale of 60% off on the course cost
RRP £120 Sale Price £50 (limited time only)
Courses will be run in central London
The website is TinmoorKettle.com
Hands on, half day course, brunch and a couple of sample beers included
Dates available:
14th December 2014
11th January 2015
18th January 2015
25th January 2015
1st February 2015
8th February 2015
15th February 2015
22nd February 2015

Logo file included, AI version available on request. Any photo on the TinmoorKettle.com site is available to be used. Simply pull of the site or I can send to you.

Colour scheme used on site: #FF9700 & #26210D

I will reply to any designs offered between 8pm and 11pm BST each day.

Good luch!

Hi everyone, We have now reviewed the first submissions and there are some ok, some good and a couple of great efforts in there. Here are the following common things that we commented on in our first reviews: 1. WHAT IS THE FLYER TRYING TO SAY... YOU'VE GOT 1 SECOND!!!! This flyer is to be given out in the street. That gives you 1second to tell the reader what the flyer is selling. That is the number 1 priority for the flyer. Please make it your priority as designers. 2. SALE SALE SALE This is the number 2 priority, people love SALES and a big colourful sticker saying SALE or 60% OFF (or both) is to be positioned so once the reader has seen that the flyer is about a craft beer brewing course, they see there is a sale on the course. 3. BRAND PERSONALITY 3rd priority is the Tinmoor Kettle brand identity. We picked this name, logo and colour scheme to stand out. Please use these to enhance points 1 & 2, but also get our logo on there is a bold and brash way. 4. USE THE BACK OF THE CARD Place any info that is not required in 1, 2 & 3 on the back, or even remove it all together if YOU feel it is not suited. You are the designer, so make some design decisions! We are happy to ask you to add things back in if we feel it is lacking. Our best guess (and we are NOT designers) is that putting either the dates OR a brief description of the course on the back would be enough info. If you think we can get bother, without overloading the page, give it a go! 5. CALL TO ACTION On the front and on the back, we want a CALL TO ACTION. Book at TinmoorKettle.com or just TinmoorKettle.com (you do not need http://www before it!!! We live in 2014 not 1994!!!) 6. MAKE IT BOLD, & THEN MAKE IT BOLDER This flyer is to stand out to a person that is handed 1 different leaflet every 2 minutes while walking down a busy London high street. We MUST stand out. Finally, thanks for all the designer so far, your efforts are greatly appreciated and we are very excited about the new revision of the design!

Target Market(s)

City living, young professionals who like to do fun things at the weekend.

Industry/Entity Type

Training

Font styles to use
Sans Serif

Colors
f78f20

Requirements
Must have
• Strong brand identity and call to action
In line with brand identity, see website www.TinmoorKettle.com

```html
<!DOCTYPE html>
<html lang="en">
<head>
<meta charset="utf-8">
<title>Intro to Craft Beer Brewing – Tinmoor Kettle</title>
<link rel="stylesheet" href="https://fonts.googleapis.com/css2?family=Fredoka:wght@600;700&display=swap">
<style>
  :root {
    --brand-orange: #f78f20;
    --brand-dark: #26210d;
    --ink-white: #ffffff;
    --sale-red: #e3201b;
    --sale-red-deep: #a80f0b;
    --bg-top: #4a4a48;
    --bg-bottom: #151515;
  }
  html, body {
    margin: 0;
    padding: 0;
    overflow: hidden;
    background: #1b1b1b;
  }
  .flyer {
    position: relative;
    width: 850px;
    height: 1200px;
    overflow: hidden;
    font-family: "Fredoka", "Arial Rounded MT Bold", sans-serif;
    color: var(--ink-white);
  }
  .brewery-photo {
    position: absolute;
    inset: 0;
    background:
      radial-gradient(ellipse at 45% 72%, rgba(0,0,0,0.75) 0%, rgba(0,0,0,0.35) 30%, rgba(0,0,0,0) 55%),
      linear-gradient(160deg, var(--bg-top) 0%, #2e2e2d 45%, var(--bg-bottom) 100%);
  }
  .frame {
    position: absolute;
    inset: 0;
  }
  .brand {
    position: absolute;
    left: 300px;
    width: 250px;
    top: 28px;
    display: flex;
    flex-direction: column;
    align-items: center;
    gap: 16px;
  }
  .brand-dot {
    width: 120px;
    height: 120px;
    border-radius: 50%;
    background: var(--brand-orange);
  }
  .brand-name {
    font-weight: 700;
    font-size: 46px;
    line-height: 48px;
    letter-spacing: 1px;
    text-align: center;
    text-transform: uppercase;
    color: var(--brand-orange);
  }
  .headline {
    position: absolute;
    left: 0;
    right: 0;
    top: 360px;
    margin: 0;
    text-align: center;
    font-weight: 700;
    font-size: 100px;
    line-height: 94px;
    text-transform: uppercase;
    letter-spacing: 1px;
  }
  .sale-sticker {
    position: absolute;
    left: 268px;
    top: 668px;
    width: 350px;
    height: 350px;
  }
  .sale-sticker svg { position: absolute; inset: 0; }
  .sale-text {
    position: absolute;
    inset: 0;
    display: flex;
    flex-direction: column;
    align-items: center;
    justify-content: center;
    font-weight: 700;
    font-size: 108px;
    line-height: 90px;
    text-transform: uppercase;
  }
  .call-to-action {
    position: absolute;
    left: 0;
    right: 0;
    top: 1138px;
    margin: 0;
    text-align: center;
    font-weight: 700;
    font-size: 29px;
    text-transform: uppercase;
    letter-spacing: 0.5px;
  }
  .call-to-action .site { color: var(--brand-orange); }
</style>
</head>
<body>
<main class="flyer">
  <div class="brewery-photo" role="img" aria-label="Dark photo of a brewery floor with steel brewing vessels and an open mash tun"></div>

  <svg class="frame" width="850" height="1200" viewBox="0 0 850 1200" aria-hidden="true">
    <g fill="none" stroke="var(--brand-orange)" stroke-width="4">
      <polyline points="290,237 76,237 76,1098 789,1098 789,237 560,237"/>
    </g>
  </svg>

  <header class="brand">
    <div class="brand-dot"></div>
    <div class="brand-name">Tinmoor<br>Kettle</div>
  </header>

  <h1 class="headline">Intro to<br>Craft Beer<br>Brewing</h1>

  <div class="sale-sticker">
    <svg viewBox="-100 -100 200 200" width="350" height="350" aria-hidden="true">
      <defs>
        <radialGradient id="sticker-fill" cx="40%" cy="35%" r="70%">
          <stop offset="0%" stop-color="var(--sale-red)"/>
          <stop offset="100%" stop-color="var(--sale-red-deep)"/>
        </radialGradient>
      </defs>
      <polygon fill="url(#sticker-fill)" points="100,0 84.7,15 94,34.2 74.5,43 76.6,64.3 55.3,65.9 50,86.6 29.4,80.8 17.4,98.5 0,86 -17.4,98.5 -29.4,80.8 -50,86.6 -55.3,65.9 -76.6,64.3 -74.5,43 -94,34.2 -84.7,15 -100,0 -84.7,-15 -94,-34.2 -74.5,-43 -76.6,-64.3 -55.3,-65.9 -50,-86.6 -29.4,-80.8 -17.4,-98.5 0,-86 17.4,-98.5 29.4,-80.8 50,-86.6 55.3,-65.9 76.6,-64.3 74.5,-43 94,-34.2 84.7,-15"/>
    </svg>
    <div class="sale-text"><span>60%</span><span>Off</span></div>
  </div>

  <p class="call-to-action">Book now at: <span class="site">TinmoorKettle.com</span></p>
</main>
</body>
</html>
```